VELMO Harvest

3-fold brochure with pictures. I will supply text and pictures for a summer mission team which will be recruited in coming weeks to go to a Native Canadian community on Vancouver Island. The goals will be to build trusting friendships, learn each other's cultures, and introduce Native youth and adults to the Bible.

```html
<!DOCTYPE html>
<html lang="en">
<head>
<meta charset="utf-8">
<title>VELMO Harvest – Summer Mission Brochure</title>
<link rel="stylesheet" href="https://fonts.googleapis.com/css2?family=Anton&family=Open+Sans:ital,wght@0,400;0,600;0,700;0,800;1,700;1,800&display=swap">
<style>
  :root{
    --navy:#1c2d5c;
    --green:#2e6a37;
    --green-dark:#1f3f26;
    --green-deep:#173221;
    --lime:#8cc63f;
    --blue:#1f5ea8;
    --white:#ffffff;
    --paper:#f7f8f5;
    --stage:#e4e5e3;
    --ink:#2b2f36;
  }
  *{box-sizing:border-box;margin:0;padding:0}
  html,body{width:804px;height:1200px;overflow:hidden}
  body{background:var(--stage);font-family:"Open Sans",Arial,sans-serif;color:var(--ink)}
  .spread{position:absolute;left:12px;width:780px;height:560px;display:flex;background:var(--white);box-shadow:0 3px 10px rgba(0,0,0,.18)}
  .spread--outside{top:20px}
  .spread--inside{top:620px}
  .panel{position:relative;width:260px;height:560px;overflow:hidden}
  .panel + .panel{border-left:1px solid #e2e2e2}
  .photo{position:absolute;left:0;width:100%}
  .brand{display:flex;align-items:center;gap:7px;font-weight:800;font-size:12px;color:var(--navy);letter-spacing:.3px;text-transform:uppercase}
  .brand__mark{width:14px;height:14px;background:var(--green)}
  .brand--light{color:var(--white)}
  .brand--light .brand__mark{background:var(--lime)}
  .headline{font-family:"Anton",Impact,sans-serif;text-transform:uppercase;line-height:1}
  .band{position:absolute;left:0;width:100%;background:var(--blue)}

  /* outside: left panel */
  .trip .brand{position:absolute;top:22px;left:20px}
  .trip .headline{position:absolute;top:60px;left:20px;width:225px;font-size:44px;color:var(--navy)}
  .trip__sub{position:absolute;top:160px;left:20px;width:225px;font-weight:800;font-style:italic;color:var(--green);font-size:18px;line-height:1.15;text-transform:uppercase}
  .trip .photo{top:240px;height:285px;background:linear-gradient(180deg,#9fb7c9 0%,#5f7f6a 45%,#2f4b3b 70%,#6c8ea3 100%)}
  .trip .band{bottom:0;height:35px}

  /* outside: middle panel */
  .contact__block{position:absolute;top:0;left:0;width:100%;height:205px;background:var(--green-deep);padding:24px 20px;color:var(--white)}
  .contact__title{font-weight:800;font-size:22px;margin-bottom:12px}
  .contact__text{font-size:12px;line-height:1.5;margin-bottom:10px}
  .contact .photo{top:205px;height:320px;background:linear-gradient(160deg,#6f8f9c 0%,#4b6a55 40%,#7d5a3c 70%,#2f3b35 100%)}
  .contact .band{bottom:0;height:35px}

  /* outside: cover */
  .cover .brand{position:absolute;top:22px;left:20px}
  .cover__title{position:absolute;top:55px;left:0;width:100%;height:82px;background:var(--green-deep);display:flex;align-items:center;justify-content:flex-end;padding-right:20px}
  .cover .headline{font-size:62px;color:var(--white)}
  .cover__date{position:absolute;top:137px;left:0;width:100%;height:40px;background:var(--green);color:var(--white);font-weight:800;font-size:20px;display:flex;align-items:center;justify-content:flex-end;padding-right:20px}
  .cover .photo{top:177px;height:321px;background:linear-gradient(180deg,#a9c3d3 0%,#6e8f7c 45%,#3d5a48 65%,#7fa0b3 100%)}
  .cover .band{bottom:0;height:62px;display:flex;align-items:center;gap:10px;padding-left:20px;color:var(--white);font-weight:800;font-size:20px}

  /* inside: impact */
  .impact{background:var(--paper)}
  .impact__tab{position:absolute;top:22px;left:0;background:var(--green);color:var(--white);font-weight:800;font-size:14px;padding:7px 20px;text-transform:uppercase;letter-spacing:.5px}
  .impact__list{position:absolute;top:70px;left:20px;width:220px;list-style:none}
  .impact__item{margin-bottom:16px}
  .impact__name{font-weight:800;font-size:14px;color:var(--navy)}
  .impact__text{font-size:11.5px;line-height:1.45}
  .impact .photo{top:335px;height:225px;background:linear-gradient(180deg,#b7c8d4 0%,#8a9a86 50%,#5b4a36 100%)}

  /* inside: community */
  .community__block{position:absolute;top:0;left:0;width:100%;height:150px;background:var(--green);padding:24px 20px;color:var(--white)}
  .community__title{font-weight:800;font-size:15px;text-transform:uppercase;letter-spacing:.5px;margin-bottom:10px}
  .community__text{font-size:12px;line-height:1.5}
  .community .photo{top:150px;height:330px;background:linear-gradient(170deg,#4a5a48 0%,#8a6a52 45%,#3a3030 100%)}
  .community__footer{position:absolute;bottom:0;left:0;width:100%;height:80px;background:var(--green-dark);display:flex;align-items:center;padding-left:20px}

  /* inside: trip details */
  .details__block{position:absolute;top:0;left:0;width:100%;height:170px;background:var(--green);padding:22px 20px;color:var(--white)}
  .details__title{font-weight:800;font-size:15px;text-transform:uppercase;letter-spacing:.5px;margin-bottom:12px}
  .details__list{list-style:none}
  .details__item{display:flex;align-items:center;gap:8px;font-size:13px;font-weight:600;margin-bottom:9px}
  .details .photo{top:170px;height:390px;background:linear-gradient(180deg,#9bb0a3 0%,#5d6f5a 40%,#6a4a38 75%,#2e2a28 100%)}
</style>
</head>
<body>

<section class="spread spread--outside" aria-label="Brochure outside">
  <div class="panel trip">
    <div class="brand"><span class="brand__mark"></span>VELMO Harvest</div>
    <h2 class="headline">This is more than a trip –</h2>
    <p class="trip__sub">It's an opportunity to transform lives!</p>
    <div class="photo" role="img" aria-label="Photo of a mountain lake on Vancouver Island"></div>
    <div class="band"></div>
  </div>

  <div class="panel contact">
    <div class="contact__block">
      <p class="contact__title">Space is limited.</p>
      <p class="contact__text">Apply by May 15 to join the team.</p>
      <p class="contact__text">Call or write to our office for an information package.</p>
    </div>
    <div class="photo" role="img" aria-label="Photo collage of a carved totem, drum and a kayak on the water"></div>
    <div class="band"></div>
  </div>

  <div class="panel cover">
    <div class="brand"><span class="brand__mark"></span>VELMO Harvest</div>
    <div class="cover__title"><h1 class="headline">Harvest</h1></div>
    <div class="cover__date">July 2-12, 2024</div>
    <div class="photo" role="img" aria-label="Photo of a kayaker paddling on a coastal inlet"></div>
    <div class="band">
      <svg width="18" height="18" viewBox="0 0 24 24" aria-hidden="true"><path fill="#fff" d="M6.6 10.8a15.1 15.1 0 0 0 6.6 6.6l2.2-2.2c.3-.3.7-.4 1-.2 1.1.4 2.3.6 3.6.6.6 0 1 .4 1 1V20c0 .6-.4 1-1 1C10.6 21 3 13.4 3 4c0-.6.4-1 1-1h3.5c.6 0 1 .4 1 1 0 1.3.2 2.5.6 3.6.1.3 0 .7-.2 1z"/></svg>
      (555) 014-2270
    </div>
  </div>
</section>

<section class="spread spread--inside" aria-label="Brochure inside">
  <div class="panel impact">
    <div class="impact__tab">Your impact</div>
    <ul class="impact__list">
      <li class="impact__item"><p class="impact__name">Empower youth</p><p class="impact__text">Share friendship and mentoring with Native young people.</p></li>
      <li class="impact__item"><p class="impact__name">Bridge cultures</p><p class="impact__text">Learn traditions and share stories across communities.</p></li>
      <li class="impact__item"><p class="impact__name">Offer hope</p><p class="impact__text">Introduce youth and adults to the Bible.</p></li>
    </ul>
    <div class="photo" role="img" aria-label="Photo of a carved wooden welcome sign at the community entrance"></div>
  </div>

  <div class="panel community">
    <div class="community__block">
      <p class="community__title">The student community</p>
      <p class="community__text">A team of young adults serving together on Vancouver Island.</p>
    </div>
    <div class="photo" role="img" aria-label="Photo of a young child from the community"></div>
    <div class="community__footer">
      <div class="brand brand--light"><span class="brand__mark"></span>VELMO Harvest</div>
    </div>
  </div>

  <div class="panel details">
    <div class="details__block">
      <p class="details__title">Trip details</p>
      <ul class="details__list">
        <li class="details__item"><svg width="12" height="12" viewBox="0 0 12 12" aria-hidden="true"><path d="M1 6l3 3 7-7" stroke="#8cc63f" stroke-width="2" fill="none"/></svg>18 years old</li>
        <li class="details__item"><svg width="12" height="12" viewBox="0 0 12 12" aria-hidden="true"><path d="M1 6l3 3 7-7" stroke="#8cc63f" stroke-width="2" fill="none"/></svg>$1,800 From Lakeview, ON</li>
        <li class="details__item"><svg width="12" height="12" viewBox="0 0 12 12" aria-hidden="true"><path d="M1 6l3 3 7-7" stroke="#8cc63f" stroke-width="2" fill="none"/></svg>10 days | July 2-12, 2024</li>
      </ul>
    </div>
    <div class="photo" role="img" aria-label="Portrait photo of a young Native woman outdoors"></div>
  </div>
</section>

</body>
</html>
```